Cutting Board Oil Label

I would like a label created for our custom made cutting board oil. The bottle will be clear and come in several different sizes. I have included the current label we use. We would like the information to stay the same, but more aesthetically pleasing and professionally presented. I am also including our logo and the current label of our biggest competitor.

```html
<!DOCTYPE html>
<html lang="en">
<head>
<meta charset="UTF-8">
<title>Laurel Hollow Goods – Cutting Board Conditioner Label</title>
<link href="https://fonts.googleapis.com/css2?family=Marcellus&family=Roboto+Condensed:wght@400;700&family=Roboto:wght@500&display=swap" rel="stylesheet">
<style>
  :root {
    --page: #f1f1f1;
    --wood: #6f4428;
    --wood-dark: #4a2c19;
    --teal: #22bcc6;
    --bark: #3b2416;
    --cream: #ead096;
    --leaf: #008f45;
    --white: #ffffff;
    --ink: #2b1a10;
  }
  * { margin: 0; padding: 0; box-sizing: border-box; }
  html, body {
    width: 1200px; height: 1200px; overflow: hidden;
    background: var(--page);
  }
  .label {
    position: absolute; left: 300px; top: 300px;
    width: 600px; height: 600px;
    border-radius: 12px; overflow: hidden;
    background: var(--wood);
  }
  .label__wood {
    position: absolute; inset: 0 0 185px 0;
    background: linear-gradient(90deg, var(--wood-dark) 0%, var(--wood) 14%, #7a4c2c 50%, var(--wood) 86%, var(--wood-dark) 100%);
  }
  .label__hero {
    position: absolute; inset: 0 0 185px 0;
    text-align: center; color: var(--white);
    font-family: 'Marcellus', serif;
  }
  .brand-name {
    position: absolute; top: 96px; left: 0; right: 0;
    font-size: 34px; line-height: 1;
  }
  .badge {
    position: absolute; top: 171px; left: 146px;
    width: 307px; height: 34px; border-radius: 8px;
    background: var(--leaf);
    font-family: 'Roboto Condensed', sans-serif; font-weight: 700;
    font-size: 24px; line-height: 34px; color: var(--white);
  }
  .product-title {
    position: absolute; top: 208px; left: 0; right: 0;
    font-size: 72px; line-height: 68px; font-weight: 400;
  }
  .product-use {
    position: absolute; top: 353px; left: 0; right: 0;
    font-size: 22px; line-height: 26px;
  }
  .directions {
    position: absolute; top: 415px; left: 0; width: 600px; height: 114px;
    background: var(--teal); color: var(--ink);
    font-family: 'Roboto Condensed', sans-serif;
    font-size: 15.4px; line-height: 16.7px;
    padding: 5px 18px 0; text-align: justify; text-align-last: center;
  }
  .directions strong { font-weight: 700; }
  .ingredients {
    position: absolute; top: 529px; left: 0; width: 600px; height: 32px;
    background: var(--bark); color: var(--cream);
    font-family: 'Roboto Condensed', sans-serif;
    font-size: 19px; line-height: 32px; text-align: center;
  }
  .ingredients strong { font-weight: 700; }
  .website {
    position: absolute; top: 561px; left: 0; width: 600px; height: 39px;
    background: var(--cream); color: var(--ink);
    font-family: 'Roboto', sans-serif; font-weight: 500;
    font-size: 20px; line-height: 39px; text-align: center;
  }
</style>
</head>
<body>
  <div class="label">
    <div class="label__wood" role="img" aria-label="Dark walnut wood grain texture"></div>
    <div class="label__hero">
      <div class="brand-name">Laurel Hollow Goods</div>
      <div class="badge">FOOD SAFE - ALL NATURAL</div>
      <h1 class="product-title">Cutting Board<br>Conditioner</h1>
      <p class="product-use">For use on cutting boards, butcher blocks,<br>wood utensils, and any other wood products</p>
    </div>
    <p class="directions"><strong>Directions:</strong> Apply a generous amount of conditioner with a clean, lint free cloth. For best results, allow board to soak in conditioner overnight. Using a clean, lint free cloth, buff and remove any excess conditioner. For new or unconditioned cutting boards, butcher blocks, or wooden kitchen utensils we recommend repeating the process a second time to ensure your wood is properly sealed. Recondition about once a month(depending on frequency of use) or when the board begins to become dry to the touch.</p>
    <p class="ingredients"><strong>Made with:</strong> Beeswax, Mineral Oil, Orange Oil, Lemon Oil, Vitamin E</p>
    <p class="website">www.LaurelHollowGoods.com</p>
  </div>
</body>
</html>
```